Bright Horizon Painting and Remodeling needs a business card

Business card should have company logo. I will upload two different logos and let me see which one is a better design for the business card.

Name of company: Bright Horizon Painting and Remodeling
Address: 4126 NW 71st st Suite 214
Miami, FL 33166

local phone: (305) 555-0142
toll free (855) 555-0197
fax (866) 555-0163

email: corinne@paintingbrighthorizon.example

not sure if i should include social media links or names on the business card.

company does interior and exterior painting, pressure washing, wall paper removal, drywall and stucco repair, staining,

We give free estimates.

I want a two sided business card.

Not sure if all this information is necessary for the business card. Designer can pick out whatever information they deem is important for a consumer to see on the business card.

Anticipating on the business card to be printed on nice quality.

I will upload an image of one of the logos on a type of business card surface. That idea can be used as well. Be creative. Business card should be professional but very nice and eye catching.

remove drywall and stucco repair and replace with tile installation

Industry/Entity Type

Business

Contact Information for Business Card

Miami, FL 33166

toll free (855) 555-0197
fax (866) 555-0163

company does interior and exterior painting, pressure washing, wall paper removal, drywall and stucco repair, staining, tile removal, *specializing in vinyl floor removal

free estimates.

Requirements
Must have
• Profesional font

```html
<!DOCTYPE html>
<html lang="en">
<head>
<meta charset="utf-8">
<title>Bright Horizon Painting and Remodeling – Business Card</title>
<link rel="stylesheet" href="https://fonts.googleapis.com/css2?family=Cinzel:wght@600&family=Open+Sans:wght@400;600&display=swap">
<style>
  :root {
    --backdrop: #636363;
    --card-front: #ffffff;
    --card-back: #f4f4f4;
    --ink: #1e1e1e;
    --purple: #8a5fd0;
    --teal: #3aa6b0;
    --green: #4fae3c;
    --lime: #c9ec5a;
    --mark-ink: #3a3a3a;
  }
  * { margin: 0; padding: 0; box-sizing: border-box; }
  html, body {
    width: 1200px; height: 900px; overflow: hidden;
    background: var(--backdrop);
    font-family: "Open Sans", Arial, sans-serif;
    color: var(--ink);
  }
  .card {
    position: absolute; top: 306px;
    width: 439px; height: 271px;
    border-radius: 10px; overflow: hidden;
  }
  .card--front { left: 149px; background: var(--card-front); }
  .card--back { left: 609px; background: var(--card-back); }

  .contact { position: absolute; left: 26px; top: 28px; }
  .contact__name {
    font-family: "Cinzel", Georgia, serif; font-weight: 600;
    font-size: 15px; letter-spacing: 1px; color: var(--purple);
    margin-bottom: 9px;
  }
  .contact__line {
    display: flex; align-items: center; gap: 5px;
    font-size: 12.5px; line-height: 18px;
  }
  .contact__icon { width: 10px; height: 10px; flex: none; }

  .company {
    position: absolute; right: 26px; top: 29px;
    text-align: right; font-size: 11.5px; line-height: 16px;
  }
  .company__name { font-weight: 600; text-transform: uppercase; }
  .company__name .accent { font-size: 15px; font-weight: 400; }
  .company__name .accent--purple { color: var(--purple); }
  .company__name .accent--teal { color: var(--teal); }
  .company__address { margin-top: 6px; font-size: 11.5px; line-height: 16px; }

  .services {
    position: absolute; right: 26px; top: 155px;
    text-align: right; text-transform: uppercase;
    font-size: 11.5px; line-height: 16px;
  }
  .services__title { color: var(--purple); font-size: 12.5px; margin-bottom: 1px; }

  .corner-art {
    position: absolute; left: 0; bottom: 0; width: 190px; height: 115px;
    background: radial-gradient(ellipse at 0% 100%,
      rgba(138,95,208,.55) 0%, rgba(58,166,176,.45) 35%,
      rgba(79,174,60,.35) 60%, rgba(201,236,90,.25) 80%, rgba(255,255,255,0) 100%);
  }

  .brand {
    position: absolute; inset: 0;
    display: flex; align-items: center; justify-content: center; gap: 12px;
  }
  .brand__dot { width: 22px; height: 22px; border-radius: 50%; background: var(--purple); flex: none; }
  .brand__name {
    font-size: 19px; font-weight: 600; color: var(--mark-ink);
    line-height: 24px; text-transform: uppercase; letter-spacing: .5px;
  }
</style>
</head>
<body>
  <section class="card card--front">
    <div class="contact">
      <p class="contact__name">Corinne</p>
      <p class="contact__line">
        <svg class="contact__icon" viewBox="0 0 10 10"><path fill="#8a5fd0" d="M1 4c0-2 2-3 4-3s4 1 4 3H7V3H3v1zM2 5h6l1 4H1z"/></svg>
        (305) 555-0142
      </p>
      <p class="contact__line">
        <svg class="contact__icon" viewBox="0 0 10 10"><path fill="#8a5fd0" d="M1 4c0-2 2-3 4-3s4 1 4 3H7V3H3v1zM2 5h6l1 4H1z"/></svg>
        (855) 555-0197 (Toll Free)
      </p>
      <p class="contact__line">
        <svg class="contact__icon" viewBox="0 0 10 10"><path fill="#8a5fd0" d="M3 1h4v3H3zM1 4h8v5H1zM3 6h4v1H3z"/></svg>
        (866) 555-0163
      </p>
      <p class="contact__line">
        <svg class="contact__icon" viewBox="0 0 10 10"><rect x="1" y="2.5" width="8" height="5.5" fill="#8a5fd0"/><path d="M1 2.5l4 3 4-3" stroke="#fff" stroke-width=".8" fill="none"/></svg>
        corinne@paintingbrighthorizon.example
      </p>
    </div>

    <div class="company">
      <p class="company__name"><span class="accent accent--purple">Bright</span> <span class="accent accent--teal">Horizon</span> Painting<br>and Remodeling</p>
      <p class="company__address">4126 NW 71st st Suite 214<br>Miami, FL 33166</p>
    </div>

    <div class="services">
      <p class="services__title">Services</p>
      <p>Interior and exterior painting,<br>Pressure washing,<br>Wall paper reomval,<br>Drywall and stucco repair,<br>Staining.</p>
    </div>

    <div class="corner-art" role="img" aria-label="Colourful paint-swatch decoration in purple, teal, green and lime"></div>
  </section>

  <section class="card card--back">
    <div class="brand">
      <span class="brand__dot"></span>
      <p class="brand__name">Bright Horizon<br>Painting and Remodeling</p>
    </div>
  </section>
</body>
</html>
```